Desktop and Networking Support Course 9.17.25

Important the ad should not be very busy with the text taking up the major part of the ad .. please do not make the text so big that it takes up most of the ad..
Flyer Design Brief for Graphic Artist
also i am looking for something unique or creative that it will stand out .
Size & Layout:
Full Page with Bleed: 8” x 10.75” + 0.25” bleed on all sides.
Footer Space: Leave a 1-inch margin at the bottom for footer content (e.g., contact info, logo, or call-to-action).
Target Audience:
College-age students (around 24 years old)
Located in the USA
Interested in creative, professional, and career-building opportunities
Purpose:
To attract students to enroll in a college program
Flyer should be eye-catching, unique, and creative
Text must be clear and readable,
Design Style:
Use vector art, typography, or photography — your choice
If using photography, feature a white young professional USA citizen:
Wearing a white collared shirt
not with long hair
Creative Direction:
The flyer should stand out visually — something people would want to look at and keep
Showcase creativity and professionalism
Use bold colors, dynamic layout, or unexpected design elements to grab attention
Avoid clutter — keep the design balanced and clean
Text Suggestions (can be adjusted):
Footer,
please leave one inch on the bottom for the footer

```html
<!DOCTYPE html>
<html lang="en">
<head>
<meta charset="UTF-8">
<title>Desktop &amp; Networking Course Flyer</title>
<link rel="stylesheet" href="https://fonts.googleapis.com/css2?family=Bebas+Neue&family=Oswald:wght@600;700&family=Poppins:wght@400;500;600;700;800&display=swap">
<style>
  :root {
    --royal: #1f4fc4;
    --royal-deep: #1a44b0;
    --gold: #e9ae0b;
    --gold-light: #f6c93a;
    --ink: #1b1b22;
    --sky-top: #a9dcf3;
    --sky-mid: #dff2fb;
    --sky-low: #9fd6f0;
    --white: #ffffff;
    --rule: #4d5563;
    --photo-light: #e6edf2;
    --photo-mid: #cfd6dc;
    --photo-dark: #3b3a42;
  }
  * { box-sizing: border-box; margin: 0; padding: 0; }
  html, body { width: 990px; height: 1200px; overflow: hidden; background: var(--white); }
  .flyer {
    position: relative; width: 990px; height: 1200px; overflow: hidden;
    font-family: "Poppins", sans-serif; color: var(--ink); background: var(--white);
  }
  .sky {
    position: absolute; left: 0; top: 0; width: 990px; height: 1075px;
    background: radial-gradient(ellipse at 35% 45%, var(--sky-mid) 0%, rgba(223,242,251,0) 55%),
                linear-gradient(180deg, var(--sky-top) 0%, var(--sky-mid) 48%, var(--sky-low) 100%);
  }
  .headline {
    position: absolute; left: 56px; top: 22px;
    font-weight: 800; color: var(--royal); font-size: 124px; line-height: 112px; letter-spacing: -2px;
  }
  .headline span { display: block; }
  .lead {
    position: absolute; left: 62px; top: 240px;
    font-size: 72px; font-weight: 400; color: var(--royal-deep); letter-spacing: 1px;
  }
  .hand {
    position: absolute; left: 63px; top: 344px; width: 92px; height: 54px;
    border-radius: 26px 30px 22px 14px; background: #f6c1a6;
  }
  .click-pill {
    position: absolute; left: 141px; top: 333px; width: 196px; height: 48px; border-radius: 24px;
    background: linear-gradient(90deg, var(--gold-light), var(--gold));
    color: var(--white); font-weight: 700; font-size: 44px; line-height: 48px; text-align: center;
    letter-spacing: 1px;
  }
  .away {
    position: absolute; left: 80px; top: 392px;
    font-size: 64px; font-weight: 500; color: var(--royal-deep); letter-spacing: 3px;
  }
  .course-band {
    position: absolute; left: 0; top: 483px; width: 760px; height: 95px; background: var(--royal);
  }
  .course-title {
    position: absolute; left: 59px; top: 12px;
    font-family: "Bebas Neue", sans-serif; font-size: 46px; color: var(--gold); line-height: 46px;
  }
  .course-sub {
    position: absolute; left: 59px; top: 57px; font-size: 24px; font-weight: 700; color: var(--white);
  }
  .stats-band {
    position: absolute; left: 0; top: 581px; width: 732px; height: 262px; background: var(--gold);
    clip-path: polygon(0 0, 100% 0, 96% 100%, 0 100%);
  }
  .rate-figure {
    position: absolute; left: 70px; top: 574px;
    font-family: "Oswald", sans-serif; font-weight: 700; color: var(--royal);
    font-size: 128px; line-height: 128px; transform: scaleX(0.82); transform-origin: left;
  }
  .rate-figure sup { font-size: 64px; font-weight: 600; vertical-align: top; line-height: 80px; }
  .rate-label { position: absolute; left: 269px; top: 603px; }
  .rate-label strong { display: block; font-size: 35px; font-weight: 800; color: var(--royal); line-height: 42px; }
  .rate-label span { display: block; font-size: 34px; font-weight: 500; line-height: 42px; }
  .stats-rule { position: absolute; left: 60px; top: 711px; width: 604px; height: 1px; background: var(--rule); }
  .stats-divider { position: absolute; left: 236px; top: 735px; width: 1px; height: 90px; background: var(--rule); }
  .prepare { position: absolute; left: 66px; top: 720px; font-size: 28px; font-weight: 500; line-height: 34px; }
  .prepare-num {
    position: absolute; left: 62px; top: 736px; font-size: 92px; font-weight: 800; color: var(--royal); line-height: 100px;
  }
  .prepare-rest { position: absolute; left: 114px; top: 752px; font-size: 34px; font-weight: 600; line-height: 34px; }
  .jobs { position: absolute; left: 269px; top: 724px; }
  .jobs strong { display: block; font-size: 35px; font-weight: 800; color: var(--royal); line-height: 38px; }
  .jobs span { display: block; font-size: 33px; font-weight: 500; line-height: 35px; }
  .features { position: absolute; left: 58px; top: 858px; width: 571px; list-style: none; }
  .features li {
    display: flex; align-items: center; height: 70px;
    font-size: 26px; font-weight: 500; border-bottom: 1px solid var(--rule);
  }
  .features li:first-child { height: 57px; }
  .features li:last-child { border-bottom: none; }
  .feature-icon { width: 42px; height: 42px; margin-right: 14px; flex: none; }
  .photo {
    position: absolute; left: 700px; top: 11px; width: 290px; height: 1064px;
    background: linear-gradient(180deg, var(--photo-light) 0%, var(--photo-mid) 55%, var(--photo-dark) 100%);
    border-radius: 140px 0 0 0;
  }
  .pill {
    position: absolute; top: 1055px; height: 51px; border-radius: 26px; border: 2px solid var(--white);
    display: flex; align-items: center; padding-left: 26px; font-size: 22px; font-weight: 500;
  }
  .pill svg { width: 24px; height: 24px; margin-right: 10px; }
  .pill-format { left: 55px; width: 414px; background: var(--gold); color: var(--ink); }
  .pill-aid { left: 516px; width: 415px; background: var(--royal); color: var(--white); }
</style>
</head>
<body>
<main class="flyer">
  <div class="sky"></div>

  <h1 class="headline"><span>YOUR</span><span>CAREER</span></h1>
  <p class="lead">Is Just a</p>
  <div class="hand" role="img" aria-label="Cartoon hand pointing at the click button"></div>
  <div class="click-pill">CLICK</div>
  <p class="away">AWAY</p>

  <section class="course-band">
    <h2 class="course-title">DESKTOP &amp; NETWORKING</h2>
    <p class="course-sub">Master Desktop OS</p>
  </section>

  <section class="stats-band"></section>
  <div class="rate-figure">90<sup>%</sup></div>
  <div class="rate-label"><strong>EMPLOYMENT RATE</strong><span>Class of 2024</span></div>
  <div class="stats-rule"></div>
  <p class="prepare">Prepare for</p>
  <div class="prepare-num">3</div>
  <p class="prepare-rest">of the<br>Top</p>
  <div class="stats-divider"></div>
  <div class="jobs"><strong>10 TECH JOBS</strong><span>National Career</span><span>Review 2025</span></div>

  <div class="photo" role="img" aria-label="Photo of a smiling young professional in a white shirt and tie holding an open laptop"></div>

  <ul class="features">
    <li>
      <svg class="feature-icon" viewBox="0 0 42 42"><circle cx="21" cy="21" r="20" fill="#1f4fc4"/><circle cx="21" cy="21" r="5" fill="none" stroke="#fff" stroke-width="2"/><path d="M21 8v8M21 26v8M8 21h8M26 21h8M12 12l5 5M30 30l-5-5" stroke="#fff" stroke-width="2"/></svg>
      Hands-On Desktop &amp; Network Training
    </li>
    <li>
      <svg class="feature-icon" viewBox="0 0 42 42"><circle cx="21" cy="21" r="20" fill="#1f4fc4"/><circle cx="19" cy="22" r="8" fill="none" stroke="#fff" stroke-width="3" stroke-dasharray="4 2"/><circle cx="19" cy="22" r="3" fill="#fff"/><path d="M26 12l2 2 4-4" stroke="#fff" stroke-width="2" fill="none"/></svg>
      Real-World Troubleshooting Skills
    </li>
    <li>
      <svg class="feature-icon" viewBox="0 0 42 42"><circle cx="21" cy="21" r="20" fill="#1f4fc4"/><circle cx="21" cy="16" r="6" fill="none" stroke="#fff" stroke-width="2"/><path d="M11 31c2-6 18-6 20 0z" fill="#fff"/></svg>
      Ready for IT Jobs
    </li>
  </ul>

  <div class="pill pill-format">
    <svg viewBox="0 0 24 24"><circle cx="12" cy="12" r="11" fill="#1f4fc4"/><path d="M7 12l3.5 3.5L17 9" stroke="#e9ae0b" stroke-width="2.5" fill="none"/></svg>
    In-Person and Remote Options
  </div>
  <div class="pill pill-aid">
    <svg viewBox="0 0 24 24"><circle cx="12" cy="12" r="11" fill="#e9ae0b"/><path d="M7 12l3.5 3.5L17 9" stroke="#1f4fc4" stroke-width="2.5" fill="none"/></svg>
    Partial Scholarships Offered
  </div>
</main>
</body>
</html>
```